Stylish Business Cards Wanted

- DOUBLE SIDED Design Required -

High end, edgy cards for a corporate and personal stylist. Must include logo,
Name: Belinda Marsh
Title: Director and Stylist
telephone : +61 8 8417 2950
email: belinda@thewardrobeledger.com
website: thewardrobeledger.com
Tag: Corporate Workwear & Uniform Specialist | Personal Stylist
Would like nice icons for telephone, email, website

Target Market(s)

Businesses wanting stylish uniforms, people wanting stylish wardrobes

Industry/Entity Type

Corporate Workwear Stylist

Contact Information for Business Card

I would like black, white and gold foiling incorporated in the design - possibly a touch of the other colours on my branding guide attached Name: Belinda Marsh Title: Director and Stylist telephone : +61 8 8417 2950 email: belinda@thewardrobeledger.com website: thewardrobeledger.com Tag: Corporate Workwear & Uniform Specialist | Personal Stylist Would like nice icons for telephone, email, website

Font styles to use
Other font styles liked:
• Raleway

Colors

Designer to choose colors to be used in the design.

Requirements
Must have
• Gold foil accents

```html
<!DOCTYPE html>
<html lang="en">
<head>
<meta charset="utf-8">
<title>The Wardrobe Ledger – Business Card</title>
<link rel="stylesheet" href="https://fonts.googleapis.com/css2?family=Raleway:wght@400;500;600;700&display=swap">
<style>
  :root {
    --canvas: #e7e3dd;
    --ink: #1c1d1d;
    --card-black: #1b1d1d;
    --card-white: #ffffff;
    --gold: #c9951f;
    --gold-edge: #d6a630;
    --grey-mark: #6e6f70;
    --divider: #8a8a8a;
    --on-dark: #f4f4f4;
  }
  * { box-sizing: border-box; margin: 0; padding: 0; }
  html, body {
    width: 1200px;
    height: 863px;
    overflow: hidden;
    background: var(--canvas);
    font-family: "Raleway", sans-serif;
    color: var(--ink);
  }
  .card {
    position: absolute;
    left: 300px;
    width: 600px;
    height: 343px;
    border-radius: 3px;
    box-shadow: 0 10px 24px rgba(0,0,0,0.18);
    border-bottom: 4px solid var(--gold-edge);
    border-right: 3px solid var(--gold-edge);
  }
  .card--front { top: 64px; background: var(--card-black); }
  .card--back { top: 456px; background: var(--card-white); }

  .brand-name {
    position: absolute;
    font-weight: 700;
    text-transform: uppercase;
    letter-spacing: 0.12em;
    white-space: nowrap;
  }
  .card--front .brand-name {
    left: 0; right: 0;
    top: 120px;
    text-align: center;
    font-size: 34px;
    color: var(--grey-mark);
  }
  .card--back .brand-name {
    right: 40px;
    top: 92px;
    font-size: 20px;
    color: var(--ink);
  }
  .tagline {
    position: absolute;
    left: 36px;
    bottom: 36px;
    font-size: 16px;
    font-weight: 500;
    color: var(--on-dark);
    letter-spacing: 0.01em;
  }

  .identity {
    position: absolute;
    left: 40px;
    top: 150px;
  }
  .identity__name {
    font-size: 30px;
    font-weight: 600;
    color: var(--ink);
    line-height: 1.1;
  }
  .identity__title {
    font-size: 15px;
    font-weight: 500;
    color: var(--gold);
    margin-top: 4px;
  }
  .divider {
    position: absolute;
    left: 290px;
    top: 150px;
    width: 1px;
    height: 118px;
    background: var(--divider);
  }
  .contact-list {
    position: absolute;
    left: 312px;
    top: 160px;
    list-style: none;
  }
  .contact-list__item {
    display: flex;
    align-items: center;
    gap: 12px;
    font-size: 16px;
    font-weight: 500;
    color: var(--ink);
    height: 32px;
  }
  .contact-list__icon {
    width: 16px;
    height: 16px;
    flex: none;
    fill: var(--ink);
  }
</style>
</head>
<body>

  <section class="card card--front" aria-label="Card front">
    <p class="brand-name">The Wardrobe Ledger</p>
    <p class="tagline">Corporate Workwear &amp; Uniform Specialist | Personal Stylist</p>
  </section>

  <section class="card card--back" aria-label="Card back">
    <div class="identity">
      <p class="identity__name">Belinda Marsh</p>
      <p class="identity__title">Director and Stylist</p>
    </div>

    <span class="divider"></span>

    <ul class="contact-list">
      <li class="contact-list__item">
        <svg class="contact-list__icon" viewBox="0 0 24 24" aria-hidden="true">
          <path d="M6.6 10.8a15.1 15.1 0 0 0 6.6 6.6l2.2-2.2a1 1 0 0 1 1-.25 11.4 11.4 0 0 0 3.6.57 1 1 0 0 1 1 1V20a1 1 0 0 1-1 1A17 17 0 0 1 3 4a1 1 0 0 1 1-1h3.5a1 1 0 0 1 1 1c0 1.25.2 2.45.57 3.57a1 1 0 0 1-.25 1z"/>
        </svg>
        +61 8 8417 2950
      </li>
      <li class="contact-list__item">
        <svg class="contact-list__icon" viewBox="0 0 24 24" aria-hidden="true">
          <path d="M2 5h20v14H2z M4 7v.4l8 5.2 8-5.2V7z" fill-rule="evenodd"/>
        </svg>
        belinda@thewardrobeledger.com
      </li>
      <li class="contact-list__item">
        <svg class="contact-list__icon" viewBox="0 0 24 24" aria-hidden="true">
          <path d="M12 2a10 10 0 1 0 0 20 10 10 0 0 0 0-20zm0 2c.9 1.2 1.6 2.6 2 4h-4c.4-1.4 1.1-2.8 2-4zM4.3 14a8 8 0 0 1 0-4h3.4a16 16 0 0 0 0 4zm.8 2h3a12 12 0 0 0 1.3 3.5A8 8 0 0 1 5.1 16zm3-8h-3a8 8 0 0 1 4.3-3.5A12 12 0 0 0 8.1 8zM12 20c-.9-1.2-1.6-2.6-2-4h4c-.4 1.4-1.1 2.8-2 4zm2.3-6H9.7a14 14 0 0 1 0-4h4.6a14 14 0 0 1 0 4zm.3 5.5A12 12 0 0 0 15.9 16h3a8 8 0 0 1-4.3 3.5zM16.3 14a16 16 0 0 0 0-4h3.4a8 8 0 0 1 0 4zm-.4-6a12 12 0 0 0-1.3-3.5A8 8 0 0 1 18.9 8z"/>
        </svg>
        www.thewardrobeledger.com
      </li>
    </ul>

    <p class="brand-name">The Wardrobe Ledger</p>
  </section>

</body>
</html>
```